WordPress Direct-Booking Website for Bend, Oregon Vacation Rental — $750 Budget
Project Overview

We are looking for a talented WordPress designer/developer to create a clean, professional and inviting direct-booking website for Cedar Lantern Retreat, an established short-term vacation rental in Bend, Oregon.

The property is currently successfully listed on Staynest and Lodgr. Our Staynest property has approximately a 4.98-star rating with more than 200 reviews, is an Staynest Guest Pick, and ranks among the Top 1% of eligible homes.

Project Budget: $750

We will select the designer based on the quality of the initial concept, understanding of the property, proposed booking solution and ability to deliver a completed and functioning WordPress website.

Existing Staynest Listing

Please use our current Staynest listing as the primary reference for photographs, property details, amenities and design inspiration:

https://www.staynest.example/rooms/48170356

Original high-resolution photographs and additional property information will be provided to the selected designer.

Design Direction

We want the website to feel:

Upscale but comfortable
Warm and welcoming
Clean and uncluttered
Pacific Northwest / Central Oregon
Professional rather than corporate
Highly visual with large property photographs
Easy to navigate
Excellent on phones, tablets and desktop computers

We welcome creativity and want designers to show us their vision for the property rather than simply copying our Staynest listing.

The website should immediately communicate that Cedar Lantern Retreat is a highly rated vacation rental in an excellent Bend location.

Key Property Features
3 bedrooms
2 bathrooms
Sleeps up to 6 guests
Pet friendly
Approximately a 5-minute walk to Bend's Tanager Quarter
Near restaurants, shopping and Brightwater Lawn Pavilion
Private fenced backyard
Covered outdoor area
Off-street driveway parking
Fireplace
Well-equipped kitchen
Staynest Premier Host
Staynest Guest Pick
Top 1% of eligible Staynest homes
Approximately 4.98 stars with 200+ guest reviews

Our location, guest reviews, cleanliness, comfort, backyard, pet-friendly accommodations and walkability should be major selling points throughout the website.

Website Structure

We anticipate approximately 6–7 pages:

Home

Large hero photograph with a strong opening message and prominent BOOK DIRECT and CHECK AVAILABILITY buttons.

The home page should quickly communicate:

CEDAR LANTERN RETREAT — BEND, OREGON

3 Bedrooms | 2 Baths | Sleeps 6 | Pet Friendly | Walk to Tanager

Our exceptional guest rating and Staynest history should also be prominently featured.

The House

Bedrooms, bathrooms, kitchen, living areas, backyard and major amenities.

Photo Gallery

Large, attractive and fast-loading photographs with an easy-to-use mobile gallery.

Location / Explore Bend

Tanager Quarter, Brightwater Lawn Pavilion, Kettleback River, restaurants, breweries, shopping, downtown Bend and nearby outdoor recreation.

Guest Reviews

Selected guest reviews and prominent presentation of our strong Staynest reputation.

Availability & Book Direct

A simple and professional direct-booking experience.

Contact / FAQ

Contact information plus common questions regarding pets, parking, check-in/check-out, cancellations and other policies.

IMPORTANT — Direct Booking & Credit Card Requirements

We want guests to be able to book directly through the website without having to contact us first.

The website should use a proven WordPress vacation-rental booking plugin or system rather than a custom-built reservation/payment system.

Guests should be able to:

Select arrival and departure dates
See available dates
Enter number of guests
See nightly charges
See cleaning fees
See applicable lodging taxes and other charges
See the complete reservation total before paying
Enter guest/contact information
Pay securely by credit or debit card
Receive an automatic reservation confirmation

Paywell is our preferred credit-card processor.

Credit-card information must be processed securely through Paywell or another established payment processor. Credit-card information should NOT be stored directly on our WordPress website.

Staynest & Lodgr Calendar Synchronization

This is very important.

The direct-booking calendar must synchronize with our existing Staynest and Lodgr calendars to reduce the possibility of double bookings.

For this single-property website, we prefer a simple solution using Staynest/Lodgr calendar or iCal synchronization rather than an expensive monthly channel-management service, if practical.

The designer should clearly identify the booking plugin/system they propose using.

IMPORTANT — Tell Us Your Proposed Booking Solution

As part of your submission, please tell us:

Which WordPress booking plugin/system you recommend.
Whether it synchronizes availability with Staynest and Lodgr.
Whether it integrates directly with Paywell.
The initial cost of the plugin/software.
Any annual or monthly fees.
Whether any additional paid software or services will be required.

We strongly prefer a solution with little or no ongoing monthly software expense.

We do not want to select a designer and later discover that the proposed booking system requires an expensive monthly subscription.

WordPress & Technical Requirements

The completed project should include:

Fully functioning WordPress website
Responsive desktop/tablet/mobile design
Fast-loading pages
Optimized photographs
SSL/HTTPS compatibility
Direct-booking functionality
Paywell payment integration
Staynest calendar synchronization
Lodgr calendar synchronization
Automatic booking confirmations
Cleaning fee and lodging-tax calculations
Contact form
Wayfind Maps/location integration
Basic spam/security protection
Wayfind Metrics capability
Basic SEO setup
Search-engine submission capability
Easy owner editing of text, rates and photographs
Search Engine Optimization

The website should be structured for Wayfind and other search engines.

Important search themes include:

Bend Oregon vacation rental
Bend Oregon vacation home
Tanager Quarter vacation rental
Vacation rental near Tanager Bend
Bend Oregon pet-friendly vacation rental
Bend vacation rental near Brightwater Lawn Pavilion
Bend Oregon direct booking vacation rental

We are not expecting an extensive ongoing SEO campaign for the $750 project. We do expect proper page titles, descriptions, headings, image optimization and a good technical foundation for future SEO.

Ownership

Upon completion and final payment:

We own the completed WordPress website.
We receive full WordPress administrator access.
We control the domain and hosting accounts.
We own all custom design files created for the project.
All necessary login credentials are provided to us.
The website can be moved to another WordPress hosting provider in the future.
There should be no proprietary dependency on the developer after completion.
What We Want From Contestants

Please review our Staynest listing before submitting your concept.

We are particularly interested in seeing an initial homepage concept showing how you would present:

Cedar Lantern Retreat
The Bend / Tanager location
Our photography
Our exceptional guest reviews and ratings
The Book Direct message
The availability/booking call-to-action

We will provide feedback on the concepts we like and work with the selected designer to refine and complete the website.

Our Goal

Our objective is straightforward:

Create a beautiful, trustworthy and easy-to-use website that encourages guests to book Cedar Lantern Retreat directly with us.

The website will complement—not replace—our existing Staynest and Lodgr listings.

We want repeat guests and new customers to have an easy way to find the property, check availability and book directly while receiving the same professional experience they expect from a major vacation-rental platform.

Target Market(s)

Consumers looking to to travel to Mexico for vacation. Family or couples

Industry/Entity Type

Short term vacation rental industry

Coding

Coded - Design and coding required

Number of Pages Required

5+ page

Requirements
Must have
• Capabilities to accept credit card payments and link to other rental property sites calendars such as LODGR and Staynets
Nice to have
• Option for best plugins for property rental

```html
<!DOCTYPE html>
<html lang="en">
<head>
<meta charset="utf-8">
<title>Cedar Lantern Retreat — Bend, Oregon Vacation Rental</title>
<link href="https://fonts.googleapis.com/css2?family=Lora:wght@400;500;600&family=Inter:wght@400;500;600&display=swap" rel="stylesheet">
<style>
:root{
  --green:#2c4433;
  --green-deep:#253b2b;
  --green-soft:#a9c39b;
  --ink:#1f2620;
  --muted:#6e716b;
  --line:#e2ddd3;
  --paper:#ffffff;
  --cream:#f8f6f1;
  --sand:#ede4d6;
  --night:#1e1f1c;
  --gold:#d9b27a;
}
*{box-sizing:border-box;margin:0;padding:0}
html,body{width:1200px;height:5055px;overflow:hidden}
body{font-family:"Inter",sans-serif;color:var(--ink);background:var(--paper);font-size:12px;line-height:1.5}
.serif{font-family:"Lora",serif}
section{position:relative;width:1200px;overflow:hidden}
.wrap{width:768px;margin:0 auto;position:relative;height:100%}
.eyebrow{font-size:9px;letter-spacing:.22em;text-transform:uppercase;font-weight:600;color:var(--ink)}
h2{font-family:"Lora",serif;font-weight:500;font-size:31px;line-height:1.28;color:var(--ink)}
.lead{font-size:11px;color:var(--muted);line-height:1.7}
.btn{display:inline-flex;align-items:center;justify-content:center;height:38px;padding:0 22px;border-radius:8px;font-size:9.5px;letter-spacing:.14em;font-weight:600;text-transform:uppercase}
.btn-solid{background:var(--green);color:#fff}
.btn-ghost{border:1.5px solid rgba(255,255,255,.8);color:#fff}
.btn-line{border:1.5px solid var(--green);color:var(--green)}
.link-arrow{display:inline-flex;align-items:center;gap:12px;font-size:9.5px;letter-spacing:.16em;font-weight:600;text-transform:uppercase}
.link-arrow::after{content:"";width:22px;height:1px;background:currentColor}
.photo{border-radius:6px}

/* nav */
.site-nav{position:absolute;top:0;left:0;width:1200px;height:56px;background:rgba(245,242,236,.92);display:flex;align-items:center;padding:0 22px;z-index:5}
.brand{font-family:"Lora",serif;font-weight:600;font-size:16px;color:var(--ink)}
.nav-links{display:flex;gap:28px;margin-left:auto;margin-right:auto;padding-left:60px;font-size:9.5px;letter-spacing:.14em;font-weight:500}
.nav-cta{background:var(--green);color:#fff;border-radius:20px;padding:8px 18px;font-size:9px;letter-spacing:.14em;font-weight:600}

/* hero */
.hero{height:660px}
.hero-photo{position:absolute;inset:0;background:
  linear-gradient(180deg,rgba(0,0,0,0) 45%,rgba(0,0,0,.55) 100%),
  linear-gradient(180deg,#c58a5b 0%,#e7a466 22%,#6f5d6b 36%,#3b3a30 48%,#5a3e24 70%,#2b2118 100%)}
.hero-badge{position:absolute;right:22px;top:82px;width:178px;padding:12px 16px;border-radius:8px;background:rgba(255,255,255,.14);color:#fff;text-align:right}
.hero-badge small{display:block;font-size:8px;letter-spacing:.12em;text-transform:uppercase;opacity:.85}
.hero-badge b{font-family:"Lora",serif;font-size:17px;font-weight:500}
.hero-badge span{display:block;font-size:8px;opacity:.8}
.hero-copy{position:absolute;left:53px;top:400px;color:#fff}
.hero-copy .eyebrow{color:#fff}
.hero-copy h1{font-family:"Lora",serif;font-weight:500;font-size:50px;line-height:1.2;margin:8px 0 6px}
.hero-sub{font-size:15px;opacity:.95}
.hero-meta{font-size:9.5px;letter-spacing:.14em;margin-top:8px}
.hero-actions{display:flex;gap:20px;margin-top:24px}

/* stats */
.stats{height:268px;text-align:center}
.stats h2{font-size:23px;padding-top:54px}
.stats .lead{width:340px;margin:10px auto 0}
.stat-row{display:flex;justify-content:center;gap:78px;margin-top:42px}
.stat b{font-family:"Lora",serif;font-weight:500;font-size:32px;color:var(--green);line-height:1}
.stat span{display:block;font-size:8px;letter-spacing:.14em;color:var(--muted);text-transform:uppercase;margin-top:6px}

/* house */
.house{height:476px;background:var(--cream)}
.house-photo{position:absolute;left:0;top:65px;width:362px;height:346px;background:linear-gradient(160deg,#7a5a3e,#b37a4b 45%,#3d2b1e)}
.rating-card{position:absolute;left:268px;top:355px;width:108px;height:66px;background:#fff;border-radius:8px;box-shadow:0 8px 24px rgba(0,0,0,.1);text-align:center;padding-top:12px}
.rating-card b{font-family:"Lora",serif;font-weight:500;font-size:20px}
.rating-card span{display:block;font-size:7.5px;letter-spacing:.14em;color:var(--muted)}
.house-copy{position:absolute;left:405px;top:66px;width:363px}
.house-copy h2{margin-top:14px}
.house-copy .lead{margin-top:16px;width:340px}
.facts{display:grid;grid-template-columns:1fr 1fr;column-gap:26px;margin-top:16px}
.fact{border-bottom:1px solid var(--line);padding:11px 0;font-family:"Lora",serif;font-size:13px}
.fact small{font-family:"Inter",sans-serif;font-size:7.5px;letter-spacing:.14em;color:var(--muted);margin-left:6px}
.house-copy .link-arrow{margin-top:28px}

/* gallery */
.gallery{height:690px;background:var(--sand)}
.gallery .eyebrow{position:absolute;top:80px}
.gallery h2{position:absolute;top:98px}
.gallery .lead{position:absolute;top:160px;width:330px}
.g-main{position:absolute;top:214px;left:0;width:507px;height:338px;background:linear-gradient(150deg,#c9ccc4,#8a6e52 45%,#4a3322 80%)}
.g-kitchen{position:absolute;top:214px;left:519px;width:249px;height:148px;background:linear-gradient(150deg,#f3efe8,#d9cbb6 60%,#5a8f86)}
.g-cabin{position:absolute;top:389px;left:519px;width:249px;height:147px;background:linear-gradient(160deg,#3d4a40,#1e2720)}
.gallery .btn{position:absolute;top:614px;height:36px;border-radius:8px}

/* location */
.location{height:466px;background:linear-gradient(180deg,#3e5866 0%,#33494f 45%,#24352c 80%,#1d2b21 100%);color:#fff}
.loc-copy{position:absolute;left:53px;top:66px}
.loc-copy .eyebrow{color:#fff;font-size:8px}
.loc-copy h2{color:#fff;margin-top:8px;font-size:29px}
.loc-copy .sub{font-size:11px;opacity:.8;margin-top:6px}
.chips{display:flex;flex-wrap:wrap;gap:8px;width:270px;margin-top:18px}
.chip{border:1px solid rgba(255,255,255,.55);border-radius:14px;padding:4px 12px;font-size:8px}
.loc-facts{display:grid;grid-template-columns:180px 140px;row-gap:14px;margin-top:22px}
.loc-fact{border-left:1px solid rgba(255,255,255,.5);padding-left:10px;font-size:8px;letter-spacing:.1em;text-transform:uppercase}
.loc-fact span{display:block;letter-spacing:0;text-transform:none;opacity:.75}
.loc-copy .link-arrow{margin-top:30px;font-size:8.5px}

/* outdoor */
.outdoor{height:492px;background:var(--paper)}
.out-copy{position:absolute;left:0;top:88px;width:360px}
.out-copy h2{margin-top:14px}
.out-copy .lead{margin-top:16px;width:330px}
.amen{display:grid;grid-template-columns:174px 174px;gap:14px 12px;margin-top:26px}
.amen div{border:1px solid var(--line);border-radius:6px;height:40px;display:flex;align-items:center;gap:8px;padding:0 12px;font-size:9px}
.amen svg{width:13px;height:13px}
.o-main{position:absolute;left:405px;top:58px;width:363px;height:212px;background:linear-gradient(170deg,#6f6a44,#9a8a5a 50%,#4b3a28)}
.o-dog{position:absolute;left:405px;top:283px;width:176px;height:146px;background:linear-gradient(160deg,#5f7650,#3b3a30)}
.o-fire{position:absolute;left:592px;top:283px;width:176px;height:146px;background:radial-gradient(circle at 50% 62%,#f2a14a 0,#8b3d1c 22%,#2a201b 55%)}

/* reviews */
.reviews{height:498px;background:var(--cream)}
.reviews .eyebrow{position:absolute;top:68px;font-size:8px}
.reviews h2{position:absolute;top:86px}
.score{position:absolute;right:0;top:78px;text-align:right}
.score b{font-family:"Lora",serif;font-weight:500;font-size:38px;color:var(--green);line-height:1}
.score small{display:block;font-size:8px;letter-spacing:.12em;color:var(--muted);margin-top:4px}
.tags{display:flex;gap:8px;justify-content:flex-end;margin-top:8px}
.tags span{background:#e8e3d8;border-radius:10px;padding:3px 10px;font-size:7px;letter-spacing:.12em;font-weight:600}
.cards{position:absolute;top:210px;left:0;display:flex;gap:16px}
.review{width:245px;height:226px;background:#fff;border:1px solid var(--line);border-radius:8px;padding:22px 22px 0;position:relative}
.review .q{font-family:"Lora",serif;font-size:14px;color:var(--muted);line-height:1}
.review p{font-size:9.5px;line-height:1.65;margin-top:14px;color:#3c403a}
.review footer{position:absolute;left:22px;right:22px;bottom:22px;border-top:1px solid var(--line);padding-top:10px;display:flex;justify-content:space-between;align-items:flex-end}
.review footer b{font-size:9px;font-weight:600;display:block}
.review footer small{font-size:7.5px;color:var(--muted)}
.stars{font-size:10px;letter-spacing:1px;color:var(--ink)}

/* booking */
.booking{height:460px;background:var(--green-deep);color:#fff}
.book-copy{position:absolute;left:0;top:120px;width:380px}
.book-copy .eyebrow{color:#fff;font-size:8px}
.book-copy h2{color:#fff;margin-top:14px}
.book-copy .desc{font-size:10.5px;opacity:.85;margin-top:18px}
.book-actions{display:flex;gap:12px;margin-top:18px}
.btn-white{background:#fff;color:var(--green)}
.book-copy .note{font-size:7.5px;letter-spacing:.12em;opacity:.4;margin-top:20px}
.panel{position:absolute;left:405px;top:62px;width:363px;height:336px;border:1px solid rgba(255,255,255,.14);background:rgba(255,255,255,.04);border-radius:10px;padding:22px}
.panel .cap{font-size:7.5px;letter-spacing:.14em;opacity:.55}
.fields{display:grid;grid-template-columns:1fr 1fr;gap:10px;margin-top:12px}
.field{height:54px;border:1px solid rgba(255,255,255,.25);border-radius:6px;padding:8px 12px;font-size:12px}
.field small{display:block;font-size:7px;letter-spacing:.14em;opacity:.55;margin-bottom:6px}
.field.full{grid-column:1/3;display:flex;justify-content:space-between;align-items:flex-end}
.field.full em{font-style:normal;font-size:7.5px;opacity:.45}
.breakdown{margin-top:26px;font-size:8.5px;opacity:.75}
.breakdown div{display:flex;justify-content:space-between;margin-bottom:4px}
.total{display:flex;justify-content:space-between;border-top:1px solid rgba(255,255,255,.18);margin-top:12px;padding-top:14px;font-size:10px;font-weight:600}
.panel .btn{width:100%;background:var(--green-soft);color:var(--green-deep);height:34px;margin-top:14px;border-radius:6px}

/* explore */
.explore{height:436px;background:var(--cream)}
.explore .eyebrow{position:absolute;top:64px;font-size:8px}
.explore h2{position:absolute;top:84px}
.places{position:absolute;top:158px;display:flex;gap:12px}
.place{width:183px;height:212px;border-radius:6px;position:relative;color:#fff;overflow:hidden}
.place div{position:absolute;left:16px;bottom:16px}
.place b{font-family:"Lora",serif;font-weight:500;font-size:13.5px;line-height:1.2;display:block}
.place small{font-size:7px;letter-spacing:.14em;opacity:.85}
.p1{background:linear-gradient(180deg,#aeb0ad,#6c6e6a 55%,#343a31)}
.p2{background:linear-gradient(180deg,#d99aa6,#9d6f8a 45%,#3e3a3b)}
.p3{background:linear-gradient(180deg,#e9e4dc,#b6aa98 55%,#3c3732)}
.p4{background:linear-gradient(180deg,#d9a36e,#b76a44 45%,#4a3a2a)}

/* cta */
.cta{height:374px;background:var(--sand);text-align:center}
.cta .eyebrow{padding-top:60px;font-size:8px}
.cta h2{font-size:40px;line-height:1.28;width:480px;margin:24px auto 0}
.cta .btn{margin-top:26px;height:40px}

/* footer */
.site-footer{height:235px;background:var(--night);color:#fff}
.foot-grid{position:absolute;top:50px;left:0;display:grid;grid-template-columns:262px 128px 138px 240px;width:768px}
.foot-grid .brand{color:#fff;font-size:14px}
.foot-grid p,.foot-grid li{font-size:8.5px;color:rgba(255,255,255,.6);list-style:none;line-height:2.1}
.foot-grid .small{line-height:1.5;margin-top:14px;width:240px}
.foot-head{font-size:7.5px;letter-spacing:.16em;color:rgba(255,255,255,.4);margin-bottom:12px}
.foot-grid a{color:#fff;font-size:9px}
.foot-base{position:absolute;left:-194px;right:-194px;bottom:22px;display:flex;justify-content:space-between;font-size:7.5px;color:rgba(255,255,255,.35)}
</style>
</head>
<body>

<section class="hero">
  <div class="hero-photo" role="img" aria-label="Covered patio with lit fire pit and lounge seating at sunset, Cascade mountains on the horizon"></div>
  <nav class="site-nav">
    <span class="brand">Cedar Lantern Retreat</span>
    <div class="nav-links"><span>HOME</span><span>THE HOUSE</span><span>GALLERY</span><span>EXPLORE BEND</span><span>REVIEWS</span><span>FAQ</span></div>
    <span class="nav-cta">BOOK DIRECT</span>
  </nav>
  <div class="hero-badge">
    <small>Staynest Guest Pick</small>
    <b>★ 4.98</b>
    <span>205+ Reviews · Top 1% of Homes</span>
  </div>
  <div class="hero-copy">
    <div class="eyebrow">Bend, Oregon</div>
    <h1>Cedar Lantern Retreat</h1>
    <div class="hero-sub">Your Bend Getaway, Steps from the Tanager Quarter</div>
    <div class="hero-meta">3 BEDROOMS • 2 BATHS • SLEEPS 6 • PET FRIENDLY</div>
    <div class="hero-actions">
      <span class="btn btn-solid">Check Availability</span>
      <span class="btn btn-ghost">Explore the House</span>
    </div>
  </div>
</section>

<section class="stats">
  <h2>A Stay Guests Keep Coming Back To</h2>
  <p class="lead">Loved for its exceptional location, thoughtful details, comfort and welcoming atmosphere.</p>
  <div class="stat-row">
    <div class="stat"><b>4.98 ★</b><span>Guest Rating</span></div>
    <div class="stat"><b>205+</b><span>Guest Reviews</span></div>
    <div class="stat"><b>Top 1%</b><span>Eligible Staynest Homes</span></div>
    <div class="stat"><b>5.0</b><span>Location Rating</span></div>
  </div>
</section>

<section class="house">
  <div class="wrap">
    <div class="house-photo photo" role="img" aria-label="Living room with brick fireplace, wrought iron chandelier and armchair"></div>
    <div class="rating-card"><b>★ 4.98</b><span>GUEST FAVORITE</span></div>
    <div class="house-copy">
      <div class="eyebrow" style="font-size:8px">The House</div>
      <h2>Everything You Need.<br>Nothing You Don’t.</h2>
      <p class="lead">A thoughtfully updated Bend home designed for comfortable stays, easy mornings and memorable evenings.</p>
      <div class="facts">
        <div class="fact">03<small>BEDROOMS</small></div>
        <div class="fact">02<small>BATHROOMS</small></div>
        <div class="fact">06<small>GUESTS</small></div>
        <div class="fact">Pet Friendly</div>
        <div class="fact">Private Fenced Yard</div>
        <div class="fact">Off-Street Parking</div>
      </div>
      <span class="link-arrow">Explore the House</span>
    </div>
  </div>
</section>

<section class="gallery">
  <div class="wrap">
    <div class="eyebrow" style="font-size:8px">Gallery</div>
    <h2>Come In. Make Yourself at Home.</h2>
    <p class="lead">Freshly updated interiors, comfortable beds, a well-equipped kitchen and thoughtful touches throughout.</p>
    <div class="g-main photo" role="img" aria-label="Stone fireplace with leather armchair between two bright windows"></div>
    <div class="g-kitchen photo" role="img" aria-label="Bright white kitchen with teal tile backsplash"></div>
    <div class="g-cabin photo" role="img" aria-label="Dark A-frame cabin among tall pine trees"></div>
    <span class="btn btn-line">View Full Gallery</span>
  </div>
</section>

<section class="location" role="img" aria-label="Pine forest silhouette under a blue evening sky">
  <div class="loc-copy">
    <div class="eyebrow">Location</div>
    <h2>Bend Is Right Outside<br>Your Door</h2>
    <div class="sub">Walk to the Tanager Quarter</div>
    <div class="chips">
      <span class="chip">Restaurants</span><span class="chip">Shopping</span><span class="chip">Riverside Paths</span><span class="chip">Brightwater Lawn Pavilion</span>
    </div>
    <div class="loc-facts">
      <div class="loc-fact">05 Min<span>Tanager Quarter</span></div>
      <div class="loc-fact">Nearby<span>Kettleback River</span></div>
      <div class="loc-fact">Walkable<span>Restaurants &amp; Shopping</span></div>
      <div class="loc-fact">Minutes<span>Downtown Bend &amp; Outdoors</span></div>
    </div>
    <span class="link-arrow">Explore Bend</span>
  </div>
</section>

<section class="outdoor">
  <div class="wrap">
    <div class="out-copy">
      <div class="eyebrow" style="font-size:8px">Outdoor Living</div>
      <h2>Room to Unwind —<br>And Bring Your Best<br>Friend</h2>
      <p class="lead">Enjoy a quiet morning coffee, an evening around the fire or some outdoor time with your four-legged companion.</p>
      <div class="amen">
        <div><svg viewBox="0 0 16 16"><circle cx="5" cy="5" r="2" fill="#6e716b"/><circle cx="11" cy="5" r="2" fill="#6e716b"/><circle cx="8" cy="11" r="3" fill="#6e716b"/></svg>Pet Friendly</div>
        <div><svg viewBox="0 0 16 16"><path d="M3 13 L8 3 L13 13 Z" fill="#5d8a4d"/></svg>Fully Fenced Backyard</div>
        <div><svg viewBox="0 0 16 16"><path d="M2 8 L8 3 L14 8 V14 H2 Z" fill="#b88a3a"/></svg>Covered Porch</div>
        <div><svg viewBox="0 0 16 16"><path d="M8 2 C12 7 12 14 8 14 C4 14 4 9 8 2 Z" fill="#e0733a"/></svg>Outdoor Fire Pit</div>
      </div>
    </div>
    <div class="o-main photo" role="img" aria-label="Two wooden Adirondack chairs on a lawn under a large pine"></div>
    <div class="o-dog photo" role="img" aria-label="Small terrier dog sitting in the backyard"></div>
    <div class="o-fire photo" role="img" aria-label="Fire pit glowing at night"></div>
  </div>
</section>

<section class="reviews">
  <div class="wrap">
    <div class="eyebrow">Guest Reviews</div>
    <h2>Loved By Guests.<br>Proven By Reviews.</h2>
    <div class="score">
      <b>4.98 ★</b>
      <small>205 GUEST REVIEWS</small>
      <div class="tags"><span>GUEST FAVORITE</span><span>TOP 1% OF HOMES</span></div>
    </div>
    <div class="cards">
      <article class="review">
        <div class="q">“</div>
        <p>This home is absolutely stunning and in the perfect location. Walking distance to the Tanager Quarter, great restaurants, and the river. The house was immaculate, well-stocked, and felt like a true home away from home. We’ll definitely be back.</p>
        <footer><div><b>Lena W.</b><small>August 2024</small></div><span class="stars">★★★★★</span></footer>
      </article>
      <article class="review">
        <div class="q">“</div>
        <p>We brought our two dogs and they had the best time in the fenced backyard. The house itself is beautifully designed — comfortable beds, a well-equipped kitchen, and the fireplace was perfect for cool Bend evenings. Highly recommend.</p>
        <footer><div><b>Owen &amp; Priya D.</b><small>July 2024</small></div><span class="stars">★★★★★</span></footer>
      </article>
      <article class="review">
        <div class="q">“</div>
        <p>Cedar Lantern Retreat lived up to every bit of its name. The location is unbeatable and the host communication was exceptional. One of the best rental experiences we’ve had in years. Already planning our return trip.</p>
        <footer><div><b>Carla H.</b><small>September 2024</small></div><span class="stars">★★★★★</span></footer>
      </article>
    </div>
  </div>
</section>

<section class="booking">
  <div class="wrap">
    <div class="book-copy">
      <div class="eyebrow">Book Your Stay</div>
      <h2>Your Bend Stay Starts<br>Here.</h2>
      <p class="desc">Check your dates, see your total and book your stay directly.</p>
      <div class="book-actions">
        <span class="btn btn-white">Check Availability</span>
        <span class="btn btn-ghost" style="border-color:rgba(255,255,255,.5)">Book Direct</span>
      </div>
      <div class="note">SECURE PAYMENT · INSTANT CONFIRMATION · DIRECT BOOKING</div>
    </div>
    <div class="panel">
      <div class="cap">SELECT YOUR DATES</div>
      <div class="fields">
        <div class="field"><small>CHECK IN</small>—</div>
        <div class="field"><small>CHECK OUT</small>—</div>
        <div class="field full"><div><small>GUESTS</small>2 guests</div><em>Max 6</em></div>
      </div>
      <div class="breakdown">
        <div><span>Nightly rate</span><span>—</span></div>
        <div><span>Cleaning fee</span><span>—</span></div>
      </div>
      <div class="total"><span>Total</span><span>—</span></div>
      <span class="btn">Check Availability</span>
    </div>
  </div>
</section>

<section class="explore">
  <div class="wrap">
    <div class="eyebrow">Explore</div>
    <h2>Bend Is Your Backyard</h2>
    <div class="places">
      <div class="place p1" role="img" aria-label="Snow-capped peak above a riverside district"><div><b>Tanager Quarter</b><small>FOOD · SHOPPING · RIVER</small></div></div>
      <div class="place p2" role="img" aria-label="Mountain at pink dusk above an outdoor venue"><div><b>Brightwater Lawn<br>Pavilion</b><small>LIVE MUSIC · EVENTS</small></div></div>
      <div class="place p3" role="img" aria-label="Bright downtown interior with pendant lights"><div><b>Downtown Bend</b><small>BREWERIES · DINING<br>SHOPPING</small></div></div>
      <div class="place p4" role="img" aria-label="Volcanic peak glowing at sunset over forest"><div><b>Central Oregon<br>Outdoors</b><small>HIKING · TRAILS · ADVENTURE</small></div></div>
    </div>
  </div>
</section>

<section class="cta">
  <div class="eyebrow">Ready to Visit?</div>
  <h2>Make Cedar Lantern Retreat Your Home Base in Bend.</h2>
  <span class="btn btn-solid">Check Availability</span>
</section>

<footer class="site-footer">
  <div class="wrap">
    <div class="foot-grid">
      <div>
        <div class="brand">Cedar Lantern Retreat</div>
        <p>Bend, Oregon</p>
        <p class="small">A thoughtfully updated Bend vacation home, steps from the Tanager Quarter.</p>
      </div>
      <div>
        <div class="foot-head">NAVIGATION</div>
        <ul><li>Home</li><li>Gallery</li><li>Reviews</li><li>FAQ</li></ul>
      </div>
      <div>
        <div class="foot-head">&nbsp;</div>
        <ul><li>The House</li><li>Explore Bend</li><li>Book Direct</li><li>Contact</li></ul>
      </div>
      <div>
        <div class="foot-head">STAY IN TOUCH</div>
        <p style="line-height:1.6">Questions about the property? We’re happy to help.</p>
        <p style="margin-top:10px"><a>Book Direct →</a></p>
      </div>
    </div>
    <div class="foot-base" style="left:0;right:0">
      <span>© 2025 Cedar Lantern Retreat · Bend, Oregon · All rights reserved</span>
      <span>★ 4.98 · Guest Pick · Top 1% of Homes</span>
    </div>
  </div>
</footer>

</body>
</html>
```